Torvel, Inc. new buisness cards - brand guide included

We need new business cards. SLEAK SIMPLE FINANCE. They must include a place for NAME, TITLE, CELL, OFFICE PHONE, EMAIL. they also must include our services across the bottom. AIR, OCEAN, FTL, LTL, EXPRESS. for reference this will be being handed to some of the most prestigious shipping companies in a america.

Target Market(s)

Finance and corporate

Contact Information for Business Card

We need new business cards. SLEAK SIMPLE FINANCE. They must include a place for NAME, TITLE, CELL, OFFICE PHONE, EMAIL. they also must include our services across the bottom. AIR, OCEAN, FTL, LTL, EXPRESS.

Requirements
Must have
• We need new business cards. SLEAK SIMPLE FINANCE. They must include a place for NAME, TITLE, CELL, OFFICE PHONE, EMAIL. they also must include our services across the bottom. AIR, OCEAN, FTL, LTL, EXPRESS.
Nice to have
• USE THE COLORS AND LOGO IN THE BRAND GUIDE :)

```html
<!DOCTYPE html>
<html lang="en">
<head>
<meta charset="UTF-8">
<title>Torvel, Inc. — Business Cards</title>
<link href="https://fonts.googleapis.com/css2?family=EB+Garamond:wght@400;500&display=swap" rel="stylesheet">
<style>
  :root {
    --canvas: #d9d9d9;
    --charcoal: #2f2f31;
    --gold: #c3b292;
    --gold-text: #a89576;
    --cream: #f3eee2;
    --ink: #2a2a2a;
  }
  * { margin: 0; padding: 0; box-sizing: border-box; }
  html, body {
    width: 1200px; height: 900px; overflow: hidden;
    background: var(--canvas);
    font-family: "EB Garamond", Georgia, serif;
  }
  .stage {
    width: 1200px; height: 900px;
    display: flex; align-items: center; justify-content: center; gap: 60px;
  }
  .card {
    position: relative;
    width: 520px; height: 298px;
    box-shadow: 0 10px 28px rgba(0,0,0,0.18);
    overflow: hidden;
  }
  .card-front { background: var(--charcoal); }
  .card-back {
    background: var(--gold);
    display: flex; align-items: center; justify-content: center;
  }
  .wordmark {
    color: var(--cream);
    font-weight: 400;
    letter-spacing: 0.14em;
    text-transform: uppercase;
  }
  .card-front .wordmark {
    position: absolute; left: 44px; top: 34px;
    font-size: 38px;
  }
  .card-back .wordmark { font-size: 52px; }
  .name-band {
    position: absolute; left: 318px; right: 0; top: 116px;
    height: 44px;
    background: var(--gold);
    padding: 5px 0 0 14px;
    color: var(--ink);
  }
  .name {
    font-size: 21px; line-height: 1; letter-spacing: 0.03em;
    text-transform: uppercase;
  }
  .title {
    font-size: 8px; letter-spacing: 0.22em; margin-top: 3px;
    text-transform: uppercase;
  }
  .contacts {
    position: absolute; left: 44px; top: 178px;
    display: flex; gap: 18px;
    color: var(--cream); font-size: 15px;
  }
  .contact { display: flex; align-items: center; gap: 6px; }
  .contact svg { width: 11px; height: 13px; fill: var(--gold); }
  .divider {
    position: absolute; left: 44px; right: 40px; top: 214px; height: 1px;
    background: linear-gradient(90deg, rgba(195,178,146,0.2), var(--gold) 50%, rgba(195,178,146,0.2));
  }
  .services {
    position: absolute; left: 44px; top: 230px;
    color: var(--gold-text); font-size: 17px; letter-spacing: 0.12em;
    text-transform: uppercase;
  }
</style>
</head>
<body>
<main class="stage">
  <section class="card card-front" aria-label="Business card front">
    <div class="wordmark">Torvel</div>
    <div class="name-band">
      <div class="name">Daniel Reyes</div>
      <div class="title">Accounting Manager</div>
    </div>
    <div class="contacts">
      <span class="contact">
        <svg viewBox="0 0 10 14" aria-hidden="true"><path d="M2 0h6a1.5 1.5 0 0 1 1.5 1.5v11A1.5 1.5 0 0 1 8 14H2A1.5 1.5 0 0 1 .5 12.5v-11A1.5 1.5 0 0 1 2 0zm0 2v9h6V2z"/></svg>
        415-0187-2290
      </span>
      <span class="contact">
        <svg viewBox="0 0 14 14" aria-hidden="true"><path d="M3 1l2.2 2.8-1.3 1.6a8 8 0 0 0 4.7 4.7l1.6-1.3L13 11l-1.6 2C6 13 1 8 1 2.6z"/></svg>
        415-736-2290
      </span>
      <span class="contact">
        <svg viewBox="0 0 14 11" aria-hidden="true"><path d="M0 0h14v11H0zm1.5 1.5L7 6l5.5-4.5z"/></svg>
        dreyes@torvelinc.com
      </span>
    </div>
    <div class="divider"></div>
    <div class="services">Air | Ocean | FTL | LTL | Express.</div>
  </section>

  <section class="card card-back" aria-label="Business card back">
    <div class="wordmark">Torvel</div>
  </section>
</main>
</body>
</html>
```